Strong, modern, clean Business Card design

Looking for a stunning, but CLEAN business card design. While we are a faith-based organization, we do NOT want this to look religious.

Industry/Entity Type

Non-Profit

Contact Information for Business Card

Dale Munroe | Lead Pastor
dale@BrightHarvestHope.org
970-555-0148
PO Box 7316
Loveland, CO 80571

Font styles to use
Serif
Sans Serif

Requirements
Should not have
• Religious imagery or symbolism

```html
<!DOCTYPE html>
<html lang="en">
<head>
<meta charset="utf-8">
<title>Bright Harvest Hope – Business Card</title>
<link rel="stylesheet" href="https://fonts.googleapis.com/css2?family=Playfair+Display:wght@400&family=Roboto+Condensed:wght@300;400&display=swap">
<style>
  :root {
    --brand-blue: #4b7893;
    --card-white: #ffffff;
    --ink-grey: #3d3d3d;
    --muted-grey: #7a7a7a;
    --backdrop: #e7e9eb;
  }
  * { box-sizing: border-box; margin: 0; padding: 0; }
  html, body {
    width: 1200px;
    height: 1000px;
    overflow: hidden;
    background: var(--backdrop);
  }
  .canvas {
    position: relative;
    width: 1200px;
    height: 1000px;
    display: flex;
    justify-content: center;
    align-items: center;
    gap: 90px;
  }
  .card {
    position: relative;
    width: 380px;
    height: 660px;
    border-radius: 26px;
    box-shadow: 0 10px 30px rgba(0,0,0,0.12);
    overflow: hidden;
  }

  /* Front */
  .card--front {
    background: var(--brand-blue);
    display: flex;
    flex-direction: column;
    align-items: center;
    padding-top: 150px;
  }
  .front__badge {
    width: 220px;
    height: 200px;
    border-radius: 42px;
    background: var(--card-white);
  }
  .front__name {
    margin-top: 34px;
    font-family: "Playfair Display", serif;
    font-weight: 400;
    font-size: 34px;
    letter-spacing: 2px;
    color: var(--card-white);
    text-transform: uppercase;
    text-align: center;
    line-height: 1.15;
  }

  /* Back */
  .card--back {
    background: var(--card-white);
    padding: 58px 36px 44px;
    display: flex;
    flex-direction: column;
  }
  .back__badge {
    align-self: center;
    width: 240px;
    height: 180px;
    border-radius: 40px;
    background: var(--brand-blue);
  }
  .back__person {
    margin-top: 80px;
    text-align: center;
  }
  .back__name {
    font-family: "Roboto Condensed", sans-serif;
    font-weight: 400;
    font-size: 34px;
    color: var(--brand-blue);
    text-transform: uppercase;
    letter-spacing: 0.5px;
  }
  .back__role {
    font-family: "Roboto Condensed", sans-serif;
    font-weight: 300;
    font-size: 17px;
    color: var(--muted-grey);
    margin-top: 2px;
    margin-left: 70px;
  }
  .back__contact {
    margin-top: auto;
    font-family: "Roboto Condensed", sans-serif;
    font-weight: 400;
    font-size: 19px;
    line-height: 1.45;
    color: var(--ink-grey);
    text-align: right;
    font-style: normal;
  }
</style>
</head>
<body>
  <main class="canvas">
    <section class="card card--front" aria-label="Card front">
      <div class="front__badge"></div>
      <p class="front__name">Bright Harvest<br>Hope</p>
    </section>

    <section class="card card--back" aria-label="Card back">
      <div class="back__badge"></div>
      <div class="back__person">
        <h1 class="back__name">Dale Munroe</h1>
        <p class="back__role">Lead Pastor</p>
      </div>
      <address class="back__contact">
        PO Box 7316&nbsp; Loveland, CO 80571<br>
        970-555-0148<br>
        dale@BrightHarvestHope.org
      </address>
    </section>
  </main>
</body>
</html>
```